KT7 (acronym stands for Kitchentrade 7)

We are a sales and marketing start up. We sell bar and beverage dispensing equipment presently and we will add foodservice equipment to our portfolio in the coming year. We like our logo but we will consider different presentations of "KT7"

Industry/Entity Type

Marketing

```html
<!DOCTYPE html>
<html lang="en">
<head>
<meta charset="utf-8">
<title>KT7 Business Card</title>
<link rel="stylesheet" href="https://fonts.googleapis.com/css2?family=Arimo:wght@400;700&display=swap">
<style>
  :root {
    --page-bg: #e8e6e3;
    --card-white: #f4f4f4;
    --card-black: #1f1d1d;
    --ink-dark: #3a3a3a;
    --ink-light: #f2f2f2;
    --shadow: rgba(0, 0, 0, 0.22);
  }
  * { box-sizing: border-box; margin: 0; padding: 0; }
  html, body {
    width: 1200px;
    height: 1023px;
    overflow: hidden;
    background: var(--page-bg);
    font-family: "Arimo", Arial, sans-serif;
  }
  .sheet {
    position: relative;
    width: 1200px;
    height: 1023px;
  }
  .card {
    position: absolute;
    left: 250px;
    width: 700px;
    height: 400px;
    box-shadow: 0 8px 24px var(--shadow);
    overflow: hidden;
  }
  .card--front { top: 90px; display: flex; }
  .card--back { top: 533px; background: var(--card-black); }

  .brand-panel {
    position: relative;
    width: 50%;
    height: 100%;
    background: var(--card-white);
    display: flex;
    align-items: center;
    justify-content: center;
  }
  .brand-panel .notch {
    position: absolute;
    right: -14px;
    top: 50%;
    width: 0;
    height: 0;
    transform: translateY(-50%);
    border-top: 14px solid transparent;
    border-bottom: 14px solid transparent;
    border-left: 14px solid var(--card-white);
    z-index: 2;
  }
  .brand-mark {
    display: flex;
    align-items: center;
    gap: 14px;
  }
  .brand-mark .square {
    width: 22px;
    height: 22px;
    background: var(--ink-dark);
  }
  .brand-mark .name {
    font-weight: 700;
    font-size: 92px;
    color: var(--ink-dark);
    letter-spacing: 2px;
    line-height: 1;
  }

  .contact-panel {
    width: 50%;
    height: 100%;
    background: var(--card-black);
    color: var(--ink-light);
    display: flex;
    flex-direction: column;
    justify-content: center;
    padding-left: 60px;
  }
  .card--back .contact-panel {
    width: 100%;
    padding-left: 380px;
  }
  .person-name {
    font-weight: 700;
    font-size: 24px;
    letter-spacing: 0.5px;
    text-transform: uppercase;
    margin-bottom: 26px;
  }
  .contact-list { list-style: none; }
  .contact-list li {
    display: flex;
    align-items: center;
    gap: 12px;
    font-size: 17px;
    line-height: 1;
    margin-bottom: 14px;
  }
  .contact-list svg {
    width: 18px;
    height: 18px;
    flex: none;
  }
</style>
</head>
<body>
<main class="sheet">

  <section class="card card--front">
    <div class="brand-panel">
      <div class="brand-mark">
        <span class="square"></span>
        <span class="name">KT7</span>
      </div>
      <span class="notch"></span>
    </div>
    <div class="contact-panel">
      <p class="person-name">Dana Mercer</p>
      <ul class="contact-list">
        <li>
          <svg viewBox="0 0 18 18" aria-hidden="true"><path fill="#f2f2f2" d="M4 2l3 3-1.6 2c1 2 2.6 3.6 4.6 4.6L12 10l3 3-2 2.5C7.5 15 3 10.5 2.5 4z"/></svg>
          1-555-010-4827
        </li>
        <li>
          <svg viewBox="0 0 18 18" aria-hidden="true"><rect x="1.5" y="4" width="15" height="10" fill="#f2f2f2"/><path d="M1.5 4l7.5 6 7.5-6" fill="none" stroke="#1f1d1d" stroke-width="1.3"/></svg>
          INFO@KT7.CA
        </li>
        <li>
          <svg viewBox="0 0 18 18" aria-hidden="true"><circle cx="9" cy="9" r="7.5" fill="#f2f2f2"/><g fill="none" stroke="#1f1d1d" stroke-width="1"><ellipse cx="9" cy="9" rx="3.2" ry="7.5"/><path d="M1.5 9h15M3 5h12M3 13h12"/></g></svg>
          WWW.KT7.CA
        </li>
      </ul>
    </div>
  </section>

  <section class="card card--back">
    <div class="contact-panel">
      <p class="person-name">Dana Mercer</p>
      <ul class="contact-list">
        <li>
          <svg viewBox="0 0 18 18" aria-hidden="true"><path fill="#f2f2f2" d="M4 2l3 3-1.6 2c1 2 2.6 3.6 4.6 4.6L12 10l3 3-2 2.5C7.5 15 3 10.5 2.5 4z"/></svg>
          1-555-010-4827
        </li>
        <li>
          <svg viewBox="0 0 18 18" aria-hidden="true"><rect x="1.5" y="4" width="15" height="10" fill="#f2f2f2"/><path d="M1.5 4l7.5 6 7.5-6" fill="none" stroke="#1f1d1d" stroke-width="1.3"/></svg>
          INFO@KT7.CA
        </li>
        <li>
          <svg viewBox="0 0 18 18" aria-hidden="true"><circle cx="9" cy="9" r="7.5" fill="#f2f2f2"/><g fill="none" stroke="#1f1d1d" stroke-width="1"><ellipse cx="9" cy="9" rx="3.2" ry="7.5"/><path d="M1.5 9h15M3 5h12M3 13h12"/></g></svg>
          WWW.KT7.CA
        </li>
      </ul>
    </div>
  </section>

</main>
</body>
</html>
```